Beauty Salon Treatment Menu & Pricing

We need a Treatment Pricelist/ Brochure made to hand out to potential & existing customers! Meadowlark Body & Makeup is a small friendly beauty salon focused on the beauty essentials such as waxing, spray tanning, facials & makeup. We have a webpage with our colour theme and style and we would like to brochure to tie in.
www.meadowlarkbodyandmakeup.example.au.
We like a brochure that is clean, simple and easy to read.

Industry/Entity Type

Beauty Salon

```html
<!DOCTYPE html>
<html lang="en">
<head>
<meta charset="utf-8">
<title>Meadowlark Body &amp; Makeup – Treatment Menu</title>
<link rel="stylesheet" href="https://fonts.googleapis.com/css2?family=Ubuntu:wght@300;400;500;700&family=Ubuntu+Condensed&display=swap">
<style>
  :root {
    --backdrop: #2e2320;
    --salon-pink: #e6334f;
    --paper-white: #ffffff;
    --text-soft: rgba(255,255,255,0.78);
    --photo-warm: #e9c9a8;
    --photo-gold: #d9b46a;
    --photo-shadow: #3b3446;
  }
  * { box-sizing: border-box; margin: 0; padding: 0; }
  html, body {
    width: 1200px; height: 1200px; overflow: hidden;
    background: var(--backdrop);
  }
  body {
    position: relative;
    font-family: "Ubuntu", "Helvetica Neue", Arial, sans-serif;
    color: var(--paper-white);
  }
  .sheet {
    position: absolute;
    top: 218px;
    width: 540px;
    height: 764px;
    background: var(--salon-pink);
    overflow: hidden;
  }
  .sheet--front { left: 40px; }
  .sheet--back { left: 620px; }

  /* Front cover */
  .cover-photo {
    position: absolute; left: 0; top: 0;
    width: 100%; height: 470px;
    background: linear-gradient(125deg, var(--photo-gold) 0%, var(--photo-warm) 35%, #f3ddd0 55%, var(--photo-shadow) 100%);
  }
  .cover-brand {
    position: absolute; left: 0; right: 0; top: 600px;
    text-align: center;
    font-weight: 300; color: var(--paper-white);
    text-transform: uppercase;
  }
  .cover-brand__name { display: block; font-size: 50px; letter-spacing: 4px; line-height: 1; }
  .cover-brand__tag { display: block; font-size: 22px; letter-spacing: 5px; margin-top: 16px; }

  /* Back price list */
  .price-columns {
    position: absolute; left: 26px; top: 24px; right: 26px;
    display: flex; gap: 26px;
  }
  .price-col--left { width: 212px; }
  .price-col--right { flex: 1; }
  .price-group { margin-bottom: 6px; }
  .price-group__title {
    font-size: 10px; font-weight: 500; text-transform: uppercase;
    letter-spacing: 0.4px; text-align: right; line-height: 13px; margin-bottom: 1px;
  }
  .price-row {
    display: flex; justify-content: space-between; gap: 6px;
    font-family: "Ubuntu Condensed", "Arial Narrow", sans-serif;
    font-size: 11px; line-height: 12px;
  }
  .price-row span:last-child, .treatment__head span:last-child, .addon-row span:last-child { white-space: nowrap; }
  .treatment { margin-bottom: 7px; }
  .treatment__head {
    display: flex; justify-content: space-between; align-items: flex-end; gap: 6px;
    font-family: "Ubuntu Condensed", "Arial Narrow", sans-serif;
    font-size: 12px; line-height: 13px;
  }
  .treatment__desc {
    font-size: 6.6px; line-height: 8.4px; color: var(--text-soft);
    margin-top: 2px; padding-right: 40px;
  }
  .section-heading {
    font-size: 10px; font-weight: 500; text-transform: uppercase;
    letter-spacing: 0.4px; text-align: center; margin-bottom: 6px;
  }
  .addon-note { font-size: 6.6px; color: var(--text-soft); margin-bottom: 4px; text-align: center; }
  .addon-row {
    display: flex; justify-content: space-between; gap: 6px;
    font-family: "Ubuntu Condensed", "Arial Narrow", sans-serif;
    font-size: 11.5px; line-height: 13px; margin-bottom: 2px;
  }
  .back-brand {
    position: absolute; left: 30px; bottom: 42px;
    font-weight: 300; text-transform: uppercase; color: var(--paper-white);
  }
  .back-brand__name { display: block; font-size: 24px; letter-spacing: 2px; line-height: 26px; }
  .back-brand__tag { display: block; font-size: 10px; letter-spacing: 3px; margin-top: 3px; margin-left: 26px; }
  .back-web { position: absolute; left: 30px; bottom: 22px; font-size: 9px; color: var(--text-soft); }
  .feature-circle {
    position: absolute; right: -20px; bottom: -20px;
    width: 150px; height: 150px; border-radius: 50%;
    border: 10px solid rgba(255,255,255,0.35);
    background: linear-gradient(140deg, #ffffff 0%, #f4ece6 50%, #e8c7ae 100%);
  }
</style>
</head>
<body>

<section class="sheet sheet--front">
  <div class="cover-photo" role="img" aria-label="Photograph of a blonde model applying mascara in front of a mirror"></div>
  <div class="cover-brand">
    <span class="cover-brand__name">Meadowlark</span>
    <span class="cover-brand__tag">Body &amp; Makeup</span>
  </div>
</section>

<section class="sheet sheet--back">
  <div class="price-columns">
    <div class="price-col price-col--left">
      <div class="price-group">
        <div class="price-group__title">Facial Waxing/ Tint</div>
        <div class="price-row"><span>Eyebrow</span><span>18.00</span></div>
        <div class="price-row"><span>Brow wax &amp; tint</span><span>30.00</span></div>
        <div class="price-row"><span>Lip or chin or sides</span><span>10.00</span></div>
        <div class="price-row"><span>Brow, lip &amp; chin</span><span>33.00</span></div>
        <div class="price-row"><span>Full Face</span><span>38.00</span></div>
        <div class="price-row"><span>Lash tint</span><span>20.00</span></div>
        <div class="price-row"><span>Brow tint</span><span>16.00</span></div>
        <div class="price-row"><span>Lash &amp; Brow tint</span><span>30.00</span></div>
      </div>
      <div class="price-group">
        <div class="price-group__title">Female Waxing</div>
        <div class="price-row"><span>Brazilian</span><span>45.00</span></div>
        <div class="price-row"><span>Extended Bik</span><span>30.00</span></div>
        <div class="price-row"><span>Basic Bikini</span><span>18.00</span></div>
        <div class="price-row"><span>Full leg</span><span>45.00</span></div>
        <div class="price-row"><span>Full Leg &amp; Basic Bikini</span><span>50.00</span></div>
        <div class="price-row"><span>½ Leg</span><span>35.00</span></div>
        <div class="price-row"><span>½ Leg &amp; Basic Bikini</span><span>45.00</span></div>
        <div class="price-row"><span>Half Leg (inc knees)</span><span>30.00</span></div>
        <div class="price-row"><span>Full Arm</span><span>30.00</span></div>
        <div class="price-row"><span>Half Arm</span><span>25.00</span></div>
        <div class="price-row"><span>Underarm</span><span>18.00</span></div>
        <div class="price-row"><span>Stomach</span><span>15.00</span></div>
        <div class="price-row"><span>Back</span><span>20.00</span></div>
        <div class="price-row"><span>Patches, from</span><span>10.00</span></div>
      </div>
      <div class="price-group">
        <div class="price-group__title">Mens Waxing</div>
        <div class="price-row"><span>Neck</span><span>25.00</span></div>
        <div class="price-row"><span>Back (includes neck)</span><span>40.00</span></div>
        <div class="price-row"><span>Chest</span><span>35.00</span></div>
        <div class="price-row"><span>Chest &amp; Stomach</span><span>40.00</span></div>
        <div class="price-row"><span>Back, Chest &amp; Stomach</span><span>75.00</span></div>
        <div class="price-row"><span>Full Leg</span><span>55.00</span></div>
        <div class="price-row"><span>Full Arm</span><span>38.00</span></div>
        <div class="price-row"><span>Underarm</span><span>20.00</span></div>
      </div>
      <div class="price-group">
        <div class="price-group__title">Tanning</div>
        <div class="price-row"><span>Full Body Spray Tan</span><span>35.00</span></div>
        <div class="price-row"><span>Half Body Spray Tan</span><span>25.00</span></div>
      </div>
      <div class="price-group">
        <div class="price-group__title">Nails</div>
        <div class="price-row"><span>Manicure</span><span>40.00</span></div>
        <div class="price-row"><span>Pedicure</span><span>50.00</span></div>
        <div class="price-row"><span>Mini Manicure (file &amp; polish)</span><span>30.00</span></div>
        <div class="price-row"><span>Polish Change</span><span>15.00</span></div>
      </div>
      <div class="price-group">
        <div class="price-group__title">Makeup</div>
        <div class="price-row"><span>Bridal Makeup</span><span>95.00</span></div>
        <div class="price-row"><span>Bridal Trial</span><span>100.00</span></div>
        <div class="price-row"><span>Formal Makeup</span><span>100.00</span></div>
        <div class="price-row"><span>Day Makeup</span><span>65.00</span></div>
        <div class="price-row"><span>Lash Application</span><span>25.00</span></div>
      </div>
    </div>

    <div class="price-col price-col--right">
      <div class="section-heading">Facials</div>
      <div class="treatment">
        <div class="treatment__head"><span>Quick Fix My Skin</span><span>65.00</span></div>
        <p class="treatment__desc">A quick skin boost with a gentle cleanse, exfoliation and mask to refresh tired skin.</p>
      </div>
      <div class="treatment">
        <div class="treatment__head"><span>Glycolic Peel Treatment</span><span>55.00</span></div>
        <p class="treatment__desc">Glycolic acid lifts dull surface cells to reveal smoother, brighter and more even skin tone.</p>
      </div>
      <div class="treatment">
        <div class="treatment__head"><span>Glycolic Microdermabrasion Treatment</span><span>100.00</span></div>
        <p class="treatment__desc">Combines a glycolic peel with microdermabrasion to refine texture, pores and fine lines.</p>
      </div>
      <div class="treatment">
        <div class="treatment__head"><span>Clear Skin Facial</span><span>80.00</span></div>
        <p class="treatment__desc">A deep cleansing facial that calms breakouts and clears congested, oily skin.</p>
      </div>
      <div class="treatment">
        <div class="treatment__head"><span>Rebalancing Vitamin A Facial</span><span>90.00</span></div>
        <p class="treatment__desc">Vitamin A rich treatment to rebalance, nourish and restore a healthy skin glow.</p>
      </div>
      <div class="treatment">
        <div class="treatment__head"><span>Marine Radiance Facial</span><span>100.00</span></div>
        <p class="treatment__desc">Marine extracts hydrate and revive the skin, leaving it soft, radiant and glowing.</p>
      </div>
      <div class="treatment">
        <div class="treatment__head"><span>Anti Stress, Sensitive<br>Skin Treatment</span><span>100.00</span></div>
        <p class="treatment__desc">A soothing facial for sensitive skin that eases redness and calms stressed skin.</p>
      </div>
      <div class="treatment">
        <div class="treatment__head"><span>Anti Ageing Hydra<br>Restore Facial</span><span>120.00</span></div>
        <p class="treatment__desc">An intensive hydrating facial that plumps the skin and softens visible signs of ageing.</p>
      </div>
      <div class="treatment">
        <div class="treatment__head"><span>Firming Lift Facial</span><span>150.00</span></div>
        <p class="treatment__desc">A lifting and firming treatment that tones the face and restores natural contour.</p>
      </div>

      <div class="section-heading" style="margin-top:6px;">Facial Add Ons</div>
      <p class="addon-note">Add any of the following to a full facial</p>
      <div class="addon-row"><span>Glycolic Peel</span><span>$20</span></div>
      <div class="addon-row"><span>Firming Lift Caviar &amp; Pearl Eye Treatment</span><span>$20</span></div>
      <div class="addon-row"><span>Firming Lift Neck &amp; Bust Treatment</span><span>$20</span></div>
      <div class="addon-row"><span>Mini Pedicure (file &amp; polish)</span><span>$30</span></div>
    </div>
  </div>

  <div class="back-brand">
    <span class="back-brand__name">Meadowlark</span>
    <span class="back-brand__tag">Body &amp; Makeup</span>
  </div>
  <div class="back-web">www.meadowlarkbodyandmakeup.example.au</div>
  <div class="feature-circle" role="img" aria-label="Photograph of smooth legs with painted toenails"></div>
</section>

</body>
</html>
```